Harlow Crest Holdings (Remodeling company) needs a logo and business card

We need a business card design for a new company. We "flip" upmarket houses (buy, remodel and sell) in the Austin, TX area. I'd like neutral colors (grey, white, gold black). I would like it to include a simple, clean logo. Our designs are modern and uncluttered and I would like that reflected in the business card design.

Target Market(s)

Young professionals, Families, Retirees. Our properties will sell for $750k+

Industry/Entity Type

Real Estate

Contact Information for Business Card

Harlow Crets Holdings
Mona Harlow
(979) 555 0142
Owner
Rolf Tandem
(512) 555 0176
Realtor

Logo Text

Harlow Crest Holdings

Font styles to use
Serif
Script

Requirements
Must have
• Simple, classic design
Nice to have
• Clean lines, modern look
Should not have
• Too traditionally

```html
<!DOCTYPE html>
<html lang="en">
<head>
<meta charset="utf-8">
<title>Harlow Crest Holdings – Business Card</title>
<link rel="stylesheet" href="https://fonts.googleapis.com/css2?family=Cinzel:wght@500&family=Pinyon+Script&display=swap">
<style>
  :root {
    --backdrop: #e9e7e2;
    --card-black: #1b1c20;
    --gold: #e3d24a;
    --gold-deep: #c9b52c;
    --ink: #1b1c20;
  }
  * { margin: 0; padding: 0; box-sizing: border-box; }
  html, body {
    width: 1200px; height: 780px; overflow: hidden;
    background: var(--backdrop);
  }
  .canvas {
    position: relative; width: 1200px; height: 780px;
    display: flex; align-items: center; justify-content: center;
  }
  .card {
    position: relative; width: 420px; height: 735px;
    background: var(--card-black);
    overflow: hidden;
    box-shadow: 0 10px 30px rgba(0,0,0,0.25);
  }
  .brand {
    position: absolute; top: 95px; left: 0; right: 0;
    text-align: center;
    font-family: "Cinzel", serif; font-weight: 500;
    color: var(--gold);
    letter-spacing: 0.06em;
  }
  .brand-main { display: block; font-size: 40px; line-height: 1.1; }
  .brand-sub { display: block; font-size: 17px; letter-spacing: 0.18em; margin-top: 4px; }
  .skyline {
    position: absolute; top: 200px; left: 0; width: 100%; height: 135px;
  }
  .gold-panel {
    position: absolute; top: 335px; left: 0; right: 0; height: 315px;
    background: linear-gradient(160deg, var(--gold) 0%, var(--gold) 60%, var(--gold-deep) 100%);
    color: var(--ink); text-align: center;
  }
  .person-name {
    font-family: "Pinyon Script", cursive;
    font-size: 58px; line-height: 1; margin-top: 40px;
  }
  .person-role {
    font-family: "Cinzel", serif; font-size: 24px; letter-spacing: 0.08em;
    margin-top: 2px;
  }
  .person-phone {
    font-family: "Cinzel", serif; font-size: 30px; margin-top: 40px;
    letter-spacing: 0.02em;
  }
  .web-band {
    position: absolute; bottom: 0; left: 0; right: 0; height: 85px;
    display: flex; align-items: center; justify-content: center;
    font-family: "Cinzel", serif; font-size: 22px; color: var(--gold);
    letter-spacing: 0.08em; text-transform: lowercase;
  }
</style>
</head>
<body>
<main class="canvas">
  <article class="card">
    <header class="brand">
      <span class="brand-main">Harlow Crest</span>
      <span class="brand-sub">Holdings</span>
    </header>

    <svg class="skyline" viewBox="0 0 420 135" preserveAspectRatio="none" role="img" aria-label="Gold city skyline silhouette rising from the black top into the gold panel">
      <defs>
        <linearGradient id="skylineFade" x1="0" y1="0" x2="0" y2="1">
          <stop offset="0" stop-color="#1b1c20"/>
          <stop offset="1" stop-color="#e3d24a"/>
        </linearGradient>
      </defs>
      <rect width="420" height="135" fill="url(#skylineFade)"/>
    </svg>

    <section class="gold-panel">
      <p class="person-name">Mona Harlow</p>
      <p class="person-role">Owner</p>
      <p class="person-phone">(979) 555 0142</p>
    </section>

    <footer class="web-band">www.harlowcrestco.com</footer>
  </article>
</main>
</body>
</html>
```